Vibrant Body Mist Fine fragance

Hello

I need 6 body mists designs.
The designs should be colorful, with great background, shocking so that people can fall in love with the product just by seeing it. The label design will be the selling point of the fragrance.
6 names are:
Almond Twilight
Plum Whisper
Velvet Jolly
Andean Papaya
Nile Guava
Tala Tala Echoes

Names could change if you have a better idea or a more touchy name
Label should include:
Fine Fragrance Mist
250 ml / 8.45oz

Ideas of body mists in the attachment

Target Market(s)

Women all ages

Requirements
Must have
• Fine Fragrance Mist
• 250ml / 8.45 oz
• Name of the fragrance should be the focus point
Nice to have
• Fruits, Paradise Background, Colors, Name of the fragrance should be the focus point

```html
<!DOCTYPE html>
<html lang="en">
<head>
<meta charset="utf-8">
<title>Plum Whisper – Fine Fragrance Mist Label</title>
<link rel="stylesheet" href="https://fonts.googleapis.com/css2?family=Great+Vibes&family=Marcellus&display=swap">
<style>
  :root {
    --bg-deep: #2a1a14;
    --bg-plum: #6e2c45;
    --bg-rose: #b05a78;
    --bg-olive: #5c5a2c;
    --bg-amber: #8a5a30;
    --oval-light: #c48a9c;
    --oval-mid: #8e4560;
    --oval-dark: #4a2030;
    --oval-stroke: #2a1418;
    --name-pink: #e064a8;
    --name-shadow: #3a0f22;
    --label-cream: #fbf2f4;
  }
  html, body {
    margin: 0;
    padding: 0;
    width: 1200px;
    height: 2400px;
    overflow: hidden;
    background: var(--bg-deep);
  }
  .label {
    position: relative;
    width: 1200px;
    height: 2400px;
    overflow: hidden;
  }
  .label-art {
    position: absolute;
    inset: 0;
    width: 1200px;
    height: 2400px;
  }
  .fragrance-name {
    position: absolute;
    margin: 0;
    font-family: "Great Vibes", cursive;
    font-weight: 400;
    color: var(--name-pink);
    text-shadow: 0 0 6px rgba(255, 200, 230, 0.35), 5px 7px 6px var(--name-shadow);
    line-height: 1;
    white-space: nowrap;
  }
  .name-first {
    left: 0;
    width: 1120px;
    text-align: center;
    top: 640px;
    font-size: 290px;
  }
  .name-second {
    left: 100px;
    width: 1000px;
    text-align: center;
    top: 960px;
    font-size: 270px;
  }
  .product-type {
    position: absolute;
    left: 0;
    width: 1200px;
    top: 2110px;
    margin: 0;
    text-align: center;
    font-family: "Great Vibes", cursive;
    font-size: 96px;
    color: var(--label-cream);
    text-shadow: 2px 3px 4px rgba(30, 10, 15, 0.6);
    line-height: 1;
  }
  .product-volume {
    position: absolute;
    left: 0;
    width: 1200px;
    top: 2270px;
    margin: 0;
    text-align: center;
    font-family: "Marcellus", serif;
    font-size: 58px;
    letter-spacing: 1px;
    color: var(--label-cream);
    text-shadow: 2px 3px 4px rgba(30, 10, 15, 0.6);
    line-height: 1;
  }
</style>
</head>
<body>
<main class="label">
  <svg class="label-art" viewBox="0 0 1200 2400" xmlns="http://www.w3.org/2000/svg">
    <defs>
      <radialGradient id="bg-glow-top" cx="0.3" cy="0.15" r="0.6">
        <stop offset="0" stop-color="var(--bg-rose)"/>
        <stop offset="0.5" stop-color="var(--bg-plum)"/>
        <stop offset="1" stop-color="var(--bg-plum)" stop-opacity="0"/>
      </radialGradient>
      <radialGradient id="bg-glow-bottom" cx="0.35" cy="0.85" r="0.55">
        <stop offset="0" stop-color="var(--bg-amber)"/>
        <stop offset="0.6" stop-color="var(--bg-plum)" stop-opacity="0.6"/>
        <stop offset="1" stop-color="var(--bg-plum)" stop-opacity="0"/>
      </radialGradient>
      <linearGradient id="bg-base" x1="0" y1="0" x2="1" y2="1">
        <stop offset="0" stop-color="var(--bg-amber)"/>
        <stop offset="0.35" stop-color="var(--bg-plum)"/>
        <stop offset="0.75" stop-color="var(--bg-olive)"/>
        <stop offset="1" stop-color="var(--bg-deep)"/>
      </linearGradient>
      <radialGradient id="oval-fill" cx="0.45" cy="0.3" r="0.75">
        <stop offset="0" stop-color="var(--oval-light)"/>
        <stop offset="0.45" stop-color="var(--oval-mid)"/>
        <stop offset="1" stop-color="var(--oval-dark)"/>
      </radialGradient>
    </defs>
    <g class="background-artwork" role="img" aria-label="Abstract swirling floral fractal artwork in plum, rose, olive and amber tones">
      <rect width="1200" height="2400" fill="url(#bg-base)"/>
      <rect width="1200" height="2400" fill="url(#bg-glow-top)"/>
      <rect width="1200" height="2400" fill="url(#bg-glow-bottom)"/>
    </g>
    <g class="name-oval">
      <ellipse cx="600" cy="1060" rx="412" ry="888" fill="url(#oval-fill)" opacity="0.92" role="img" aria-label="Soft abstract swirls in blush and plum behind the fragrance name"/>
      <ellipse cx="600" cy="1060" rx="412" ry="888" fill="none" stroke="var(--oval-stroke)" stroke-width="5" stroke-dasharray="18 10"/>
    </g>
  </svg>

  <h1 class="fragrance-name name-first">Plum</h1>
  <p class="fragrance-name name-second">Whisper</p>
  <p class="product-type">Fine Fragrance Mist</p>
  <p class="product-volume">250 ML / 8.5 OZ</p>
</main>
</body>
</html>
```